Plonkara

We need a design for a mobile app (Android & iOS) with the following features:
- Recommend other applications based on different criteria, such as similar applications, hot apps, apps installed by friends and so on.
- Recommend a featured app everyday.
- List installed apps on the device.
- List harmful or malicious installed apps on the device
- List hot apps according to the more used apps by the comunity or the user's friends
- Profiles: Save the list of apps installed on the device as a list to allow the user to restore them on other devices.

Industry/Entity Type

Android

Requirements
Must have
• Find attached to this project a mockup of the screen elements desired.
To put it in a nutshell, the main elements are:
- Main Menu: A main menu to access the other modules of the app

- Recommended Apps: List of apps recommended, each app will display: icon, title, price, the reason(s) why it was recommended (can be expandable if takes too much room), a button to install and a button to ignore the advice.

- Application of the day: A screen that contains the icon of the app, its rating, some screenshots, a short description or promotional text, and a button to install the app. It must be also available a way to display the history and see the recommended applications the previous days.

- Installed Apps: A list with the apps on the device. It will show the app's icon, name, package, size and a button to share the app.

- Harmful apps: List of dangerous apps found on the device. It will show the icon of the app and the name. A visual and textual indicator to measure the dangerous, and the reasons of the report. It will also includes a button to ignore the advice and another one to uninstall the application.

- Login/My account: These screens will be used to login and manage the account. The account management options are listed on the attached document.

- Profiles: The design must include the proper screens and dialogs to: save a profile, restore a profile (install the missing apps on the device), show the apps saved on the profile.

- Hot Apps: The app must allow to filter between the hot apps and the hot apps installed by the user's friends. For each app, must show: the icon, name and a trending indicator in order to say if the app is winning or losing popularity

- Miscellaneous: Other features required:
+ Login screen: The login is made in two steps. First, the user introduce their email. If the email is already registered, enters the password. Otherwise, register a new account introducing a password twice (password + repeat password, please check the attached file for more info).
+ Password recovery and password change screens
+ Loading splash (shown at the start of the application for 2-4 seconds)
+ A proper layout to inform about errors / messages in empty lists, (for example if no harmful apps where found).
+ A proper layout for loading process, for example when scanning for harmful apps.
+ Vectorial App Icon: At least one icon for the app (512 x512 px)
+ Vectorial Featured (1024x500 px) and Promo banners (180x120 px) for Veltrano Shop.
+ For the UI elements like buttons or checkboxes is required the following status: normal, pressed, disabled and focused.
Nice to have
• Examples of apps with nice designs:

Brimwell: https://shop.veltrano.example/items/details?id=com.brimwell
Tidal Ledger: https://shop.veltrano.example/items/details?id=com.marvesto.tidal
KOV Coastal Terminals: https://tunestack.example/es/app/kov-coastal-terminals/id804172259?mt=8
Should not have
• The app should not have garish or poorly contrasted colors and icons.

```html
<!DOCTYPE html>
<html lang="en">
<head>
<meta charset="utf-8">
<title>Plonkara – Main Menu Themes</title>
<link rel="stylesheet" href="https://fonts.googleapis.com/css2?family=Nunito+Sans:wght@300;400&display=swap">
<style>
  :root {
    --stage-light: #f4f4f4;
    --stage-dark: #b9b9b9;
    --charcoal: #333333;
    --charcoal-deep: #262626;
    --teal: #00a99d;
    --teal-bright: #16b3a6;
    --teal-deep: #0b7d72;
    --teal-night: #1b3431;
    --icon: #55c2b3;
    --text: #ffffff;
    --rule-dark: rgba(0, 0, 0, 0.45);
    --rule-light: rgba(255, 255, 255, 0.12);
  }
  * { box-sizing: border-box; margin: 0; padding: 0; }
  html, body { width: 1200px; height: 684px; overflow: hidden; }
  body {
    position: relative;
    font-family: "Nunito Sans", sans-serif;
    font-weight: 300;
    color: var(--text);
    background: radial-gradient(ellipse 70% 90% at 50% 45%, var(--stage-light) 0%, #dcdcdc 60%, var(--stage-dark) 100%);
  }
  .symbols { position: absolute; width: 0; height: 0; }

  .screen {
    position: absolute;
    width: 376px;
    height: 641px;
    display: flex;
    flex-direction: column;
    box-shadow: 0 0 0 1px rgba(0,0,0,0.15);
  }
  .screen--charcoal { left: 8px; top: 12px; background: var(--charcoal); }
  .screen--teal { left: 403px; top: 15px; background: var(--teal); }
  .screen--night {
    left: 800px; top: 15px;
    background: linear-gradient(180deg, var(--teal-night) 2%, #15574f 20%, var(--teal-deep) 45%, var(--teal-deep) 70%, #0f5e56 88%, var(--teal-night) 100%);
  }

  .app-bar {
    height: 46px;
    flex: none;
    display: flex;
    align-items: center;
    justify-content: space-between;
    padding: 0 10px;
    background: linear-gradient(180deg, var(--teal-bright) 0%, var(--teal-deep) 100%);
    box-shadow: 0 1px 0 rgba(0,0,0,0.35);
  }
  .screen--night .app-bar { background: linear-gradient(180deg, #3a3a3a 0%, var(--charcoal-deep) 100%); }
  .app-bar__title { font-size: 24px; font-weight: 400; letter-spacing: 0.2px; }
  .app-bar__button { width: 32px; height: 32px; display: block; }

  .tagline {
    height: 115px;
    flex: none;
    padding-top: 24px;
    text-align: center;
    font-size: 17.5px;
    line-height: 26px;
  }

  .menu { list-style: none; margin: 0 4px; }
  .menu__item {
    height: 63.5px;
    display: flex;
    align-items: center;
    border-top: 2px solid var(--rule-dark);
    box-shadow: inset 0 1px 0 var(--rule-light);
    font-size: 21px;
  }
  .menu__item:last-child { border-bottom: 2px solid var(--rule-dark); }
  .menu__icon { width: 40px; height: 40px; margin-left: 22px; margin-right: 31px; flex: none; color: var(--icon); }
  .menu__end { height: 2px; margin: 0 4px; box-shadow: 0 1px 0 var(--rule-light); }
</style>
</head>
<body>

<svg class="symbols" aria-hidden="true">
  <defs>
    <symbol id="icon-back" viewBox="0 0 32 32">
      <circle cx="16" cy="16" r="14" fill="none" stroke="#fff" stroke-width="2.6"/>
      <path d="M22.5 16H10.5M15.5 10.5 10 16l5.5 5.5" fill="none" stroke="#fff" stroke-width="2.8" stroke-linecap="round" stroke-linejoin="round"/>
    </symbol>
    <symbol id="icon-settings" viewBox="0 0 32 32">
      <circle cx="16" cy="16" r="15" fill="#fff"/>
      <g fill="#333">
        <circle cx="16" cy="16" r="7.5"/>
        <rect x="13.8" y="5.5" width="4.4" height="21" rx="1"/>
        <rect x="13.8" y="5.5" width="4.4" height="21" rx="1" transform="rotate(45 16 16)"/>
        <rect x="13.8" y="5.5" width="4.4" height="21" rx="1" transform="rotate(90 16 16)"/>
        <rect x="13.8" y="5.5" width="4.4" height="21" rx="1" transform="rotate(135 16 16)"/>
      </g>
      <circle cx="16" cy="16" r="3.2" fill="#fff"/>
    </symbol>
    <symbol id="icon-award" viewBox="0 0 40 40">
      <path d="M13 17 8 38l6-4 4 5 3-19zM27 17l5 21-6-4-4 5-3-19z" fill="currentColor"/>
      <circle cx="20" cy="11" r="9.5" fill="currentColor"/>
      <circle cx="20" cy="11" r="6.5" fill="#2f2f2f"/>
      <path d="m20 6.5 1.4 3 3.2.3-2.4 2.1.8 3.1L20 13.4l-3 1.6.8-3.1-2.4-2.1 3.2-.3z" fill="#fff"/>
    </symbol>
    <symbol id="icon-calendar" viewBox="0 0 40 40">
      <rect x="0" y="6" width="40" height="7" fill="currentColor" opacity="0.75"/>
      <rect x="0" y="14" width="40" height="20" fill="currentColor"/>
      <text x="20" y="31" text-anchor="middle" font-family="Nunito Sans, sans-serif" font-size="17" font-weight="400" fill="#fff">31</text>
    </symbol>
    <symbol id="icon-download-file" viewBox="0 0 40 40">
      <path d="M7 3h18l8 8v27H7z" fill="currentColor"/>
      <path d="M20 14v15M14 23l6 6 6-6" fill="none" stroke="#fff" stroke-width="3" stroke-linecap="round" stroke-linejoin="round"/>
    </symbol>
    <symbol id="icon-blocked" viewBox="0 0 40 40">
      <circle cx="20" cy="20" r="14.5" fill="none" stroke="currentColor" stroke-width="5"/>
      <path d="M10 30 30 10" stroke="currentColor" stroke-width="5"/>
    </symbol>
    <symbol id="icon-person" viewBox="0 0 40 40">
      <circle cx="20" cy="11" r="8" fill="currentColor"/>
      <path d="M1 37c0-9 8-15 19-15s19 6 19 15z" fill="currentColor"/>
      <path d="M16 22h8l-4 5z" fill="#fff" opacity="0.35"/>
    </symbol>
    <symbol id="icon-document" viewBox="0 0 40 40">
      <path d="M6 2h19l9 9v28H6z" fill="currentColor"/>
      <rect x="10" y="26" width="20" height="3" fill="#fff"/>
    </symbol>
    <symbol id="icon-star" viewBox="0 0 40 40">
      <path d="m20 2 5.3 11.5 12.5 1.4-9.3 8.5 2.6 12.4L20 29.4 8.9 35.8l2.6-12.4-9.3-8.5 12.5-1.4z" fill="currentColor"/>
    </symbol>
  </defs>
</svg>

<section class="screen screen--charcoal" aria-label="Main menu, charcoal theme">
  <header class="app-bar">
    <svg class="app-bar__button" aria-label="Back"><use href="#icon-back"/></svg>
    <h1 class="app-bar__title">Plonkara</h1>
    <svg class="app-bar__button" aria-label="Settings"><use href="#icon-settings"/></svg>
  </header>
  <p class="tagline">“Lorem ipsum dolor sit amet,<br>consectetur adipisicing elit do ”</p>
  <ul class="menu">
    <li class="menu__item"><svg class="menu__icon"><use href="#icon-award"/></svg>Recommended Apps</li>
    <li class="menu__item"><svg class="menu__icon"><use href="#icon-calendar"/></svg>App of the day</li>
    <li class="menu__item"><svg class="menu__icon"><use href="#icon-download-file"/></svg>Installed apps</li>
    <li class="menu__item"><svg class="menu__icon"><use href="#icon-blocked"/></svg>Harmful apps</li>
    <li class="menu__item"><svg class="menu__icon"><use href="#icon-person"/></svg>My account</li>
    <li class="menu__item"><svg class="menu__icon"><use href="#icon-document"/></svg>Profiles</li>
    <li class="menu__item"><svg class="menu__icon"><use href="#icon-star"/></svg>Hot apps</li>
  </ul>
</section>

<section class="screen screen--teal" aria-label="Main menu, teal theme">
  <header class="app-bar">
    <svg class="app-bar__button" aria-label="Back"><use href="#icon-back"/></svg>
    <h1 class="app-bar__title">Plonkara</h1>
    <svg class="app-bar__button" aria-label="Settings"><use href="#icon-settings"/></svg>
  </header>
  <p class="tagline">“Lorem ipsum dolor sit amet,<br>consectetur adipisicing elit do ”</p>
  <ul class="menu">
    <li class="menu__item"><svg class="menu__icon"><use href="#icon-award"/></svg>Recommended Apps</li>
    <li class="menu__item"><svg class="menu__icon"><use href="#icon-calendar"/></svg>App of the day</li>
    <li class="menu__item"><svg class="menu__icon"><use href="#icon-download-file"/></svg>Installed apps</li>
    <li class="menu__item"><svg class="menu__icon"><use href="#icon-blocked"/></svg>Harmful apps</li>
    <li class="menu__item"><svg class="menu__icon"><use href="#icon-person"/></svg>My account</li>
    <li class="menu__item"><svg class="menu__icon"><use href="#icon-document"/></svg>Profiles</li>
    <li class="menu__item"><svg class="menu__icon"><use href="#icon-star"/></svg>Hot apps</li>
  </ul>
</section>

<section class="screen screen--night" aria-label="Main menu, night theme">
  <header class="app-bar">
    <svg class="app-bar__button" aria-label="Back"><use href="#icon-back"/></svg>
    <h1 class="app-bar__title">Plonkara</h1>
    <svg class="app-bar__button" aria-label="Settings"><use href="#icon-settings"/></svg>
  </header>
  <p class="tagline">“Lorem ipsum dolor sit amet,<br>consectetur adipisicing elit do ”</p>
  <ul class="menu">
    <li class="menu__item"><svg class="menu__icon"><use href="#icon-award"/></svg>Recommended Apps</li>
    <li class="menu__item"><svg class="menu__icon"><use href="#icon-calendar"/></svg>App of the day</li>
    <li class="menu__item"><svg class="menu__icon"><use href="#icon-download-file"/></svg>Installed apps</li>
    <li class="menu__item"><svg class="menu__icon"><use href="#icon-blocked"/></svg>Harmful apps</li>
    <li class="menu__item"><svg class="menu__icon"><use href="#icon-person"/></svg>My account</li>
    <li class="menu__item"><svg class="menu__icon"><use href="#icon-document"/></svg>Profiles</li>
    <li class="menu__item"><svg class="menu__icon"><use href="#icon-star"/></svg>Hot apps</li>
  </ul>
</section>

</body>
</html>
```